i need a template design for online store

hi great designers, i need a template for any online store. But preferably well owned shopping carts. I would be an added advantage if the store is setup for me. I need a mature and attractive colours. My online store deals in electronics.

Industry/Entity Type

Shopping

Number of Pages Required

1 page

```html
<!DOCTYPE html>
<html lang="en">
<head>
<meta charset="utf-8">
<title>Electronics Store Template</title>
<link href="https://fonts.googleapis.com/css2?family=Lato:ital,wght@0,400;0,700;1,400&family=Open+Sans:wght@400;600;700&display=swap" rel="stylesheet">
<style>
  :root {
    --header: #1f5b8c;
    --band-a: #2a71aa;
    --band-b: #1f6399;
    --slider: #5a9fd4;
    --menu-dark: #0e2d48;
    --menu-hover: #17426a;
    --menu-active: #3d8fd0;
    --page: #fdfcf4;
    --accent: #4d9ad4;
    --link: #3b8fd0;
    --thumb: #3f3f3f;
    --panel: #cfe3f3;
    --panel-head: #1f5f99;
    --text: #333333;
    --muted: #9a9a9a;
    --alert: #e0404a;
    --gold: #d9a02e;
    --white: #ffffff;
    --footer-text: #6a6a6a;
    --badge-line: #8e8e8e;
  }
  * { box-sizing: border-box; margin: 0; padding: 0; }
  html, body { width: 1200px; height: 1045px; overflow: hidden; }
  body { background: var(--page); font-family: 'Lato', sans-serif; color: var(--text); position: relative; }
  .abs { position: absolute; }

  /* header */
  .site-header { position: absolute; left: 0; top: 0; width: 1200px; height: 99px; background: var(--header); }
  .brand { left: 311px; top: 22px; font: 700 30px 'Open Sans', sans-serif; color: var(--white); letter-spacing: 1px; }
  .main-nav a { position: absolute; top: 78px; font-size: 9.5px; color: var(--white); text-decoration: none; }
  .cart { left: 799px; top: 68px; }
  .cart-text { left: 834px; top: 72px; font-size: 11.5px; font-style: italic; color: #a9cdea; }
  .cart-text .new { color: var(--alert); }

  /* dropdown */
  .dropdown { background: var(--menu-dark); font-size: 6px; color: var(--white); }
  .dropdown div { height: 17px; line-height: 17px; padding-left: 10px; position: relative; }
  .dropdown .hover { background: var(--menu-hover); }
  .dropdown .active { background: var(--menu-active); font-weight: 700; }
  .dropdown .sub::after { content: "›"; position: absolute; right: 6px; font-size: 10px; }
  .menu-main { left: 388px; top: 99px; width: 99px; padding: 1px 0 6px; z-index: 3; }
  .menu-sub { left: 487px; top: 131px; width: 100px; padding: 1px 0 6px; z-index: 3; }

  /* hero */
  .side-cats { left: 0; top: 99px; width: 137px; }
  .side-cats div, .slide-titles div { height: 62.2px; position: relative; color: var(--white); }
  .side-cats div { font-size: 11.5px; }
  .side-cats span { position: absolute; left: 25px; bottom: 10px; }
  .side-cats div:last-child span { bottom: 8px; }
  .band-a { background: var(--band-a); }
  .band-b { background: var(--band-b); }
  .slider { left: 137px; top: 99px; width: 925px; height: 311px; background: var(--slider); }
  .slider-caption { left: 0; width: 925px; top: 272px; text-align: center; font: 700 15px 'Open Sans', sans-serif; color: var(--white); }
  .slider-arrows { left: 876px; top: 273px; }
  .slide-titles { left: 1062px; top: 99px; width: 138px; height: 311px; background: var(--band-b); }
  .slide-titles span { position: absolute; left: 8px; bottom: 10px; font: 700 11.5px 'Open Sans', sans-serif; }

  /* categories panel */
  .categories { left: 19px; top: 453px; width: 187px; height: 258px; background: var(--panel); border-radius: 2px; border-top: 2px solid #a9cbe8; }
  .categories h2 { height: 39px; background: var(--panel-head); color: var(--white); font: 700 13.5px Arial, sans-serif; text-align: center; line-height: 39px; letter-spacing: -0.2px; }
  .categories ul { list-style: none; margin: 12px 0 0 30px; width: 157px; }
  .categories li { font-size: 9.5px; color: #555; height: 18.4px; line-height: 16px; padding-left: 19px; border-bottom: 1px dotted #8aa8c2; }
  .more-link { left: 19px; top: 223px; font-size: 9.5px; color: #d2242b; text-decoration: underline; }

  /* product grid */
  .product { width: 207px; height: 51px; background: var(--white); border: 1px solid #dcdcdc; }
  .product.bare { background: none; border-color: transparent; }
  .product .thumb { position: absolute; left: -1px; top: -1px; width: 52px; height: 51px; background: var(--thumb); }
  .product .name { position: absolute; left: 63px; top: 10px; font-size: 10px; font-weight: 700; color: var(--link); }
  .product .price { position: absolute; left: 63px; top: 29px; font-size: 10.5px; }
  .product .old { color: #999; font-style: italic; text-decoration: line-through; margin-right: 10px; }
  .badge { position: absolute; right: -1px; top: -1px; width: 40px; height: 21px; background: var(--accent); color: var(--white); font-size: 12px; text-align: center; line-height: 21px; }

  /* recent */
  .recent { left: 976px; top: 451px; width: 210px; }
  .recent h3 { font-size: 12.5px; font-weight: 400; color: #222; margin-bottom: 14px; }
  .recent-item { position: relative; height: 25.4px; }
  .recent-item .sq { position: absolute; left: 2px; top: 2px; width: 17px; height: 17px; background: var(--thumb); }
  .recent-item .t { position: absolute; left: 38px; top: 0; font-size: 8.5px; font-weight: 700; color: var(--link); }
  .recent-item .ago { position: absolute; left: 38px; top: 11px; font-size: 6.5px; color: var(--muted); }
  .recent-item .p { position: absolute; left: 190px; top: 3px; font-size: 9px; font-weight: 700; color: #222; }
  .recent-item.gold .t, .recent-item.gold .p { color: var(--gold); }

  /* articles */
  .article { top: 757px; width: 187px; }
  .article .media { width: 187px; height: 103px; background: var(--slider); border-bottom: 3px solid #c8dcec; }
  .article h4 { height: 30px; padding-top: 14px; font-size: 9.5px; font-weight: 700; }
  .article h4.link { color: #1f5b8c; text-decoration: underline; }
  .article p { font-size: 7.6px; line-height: 11.4px; text-align: justify; color: #333; }

  /* footer */
  .footer-links, .copyright { right: 445px; width: 380px; text-align: right; font: 400 8.5px 'Open Sans', sans-serif; color: var(--footer-text); letter-spacing: -0.1px; white-space: nowrap; }
  .footer-links { top: 992px; }
  .footer-links span { margin: 0 5px; }
  .copyright { top: 1010px; }
  .copyright u { color: #6a7a10; }
  .footer-rule { left: 774px; top: 987px; width: 1px; height: 45px; background: #d8d8d8; }
  .pay-badges { left: 797px; top: 994px; }
</style>
</head>
<body>

<header class="site-header">
  <div class="abs brand">LOGO</div>
  <nav class="main-nav">
    <a style="left:311px">Home</a>
    <a style="left:411px">Categories</a>
    <a style="left:503px">Popular</a>
    <a style="left:587px">Our choise</a>
    <a style="left:675px">More</a>
  </nav>
  <svg class="abs cart" width="26" height="22" viewBox="0 0 26 22" aria-hidden="true">
    <path d="M1 2h4l3 12h13l3-9H7" fill="none" stroke="#fff" stroke-width="2"/>
    <path d="M9 8h13M10 11h10" stroke="#fff" stroke-width="1.5"/>
    <circle cx="10" cy="18" r="2" fill="#fff"/><circle cx="19" cy="18" r="2" fill="#fff"/>
  </svg>
  <div class="abs cart-text">(3 items) <span class="new">(+2 new)</span></div>
</header>

<section class="abs side-cats">
  <div class="band-a"><span>Man</span></div>
  <div class="band-b"><span>Women</span></div>
  <div class="band-a"><span>Child</span></div>
  <div class="band-b"><span>Accessories</span></div>
  <div class="band-b"><span>Specials</span></div>
</section>

<section class="abs slider" role="img" aria-label="Featured electronics product slide">
  <div class="abs slider-caption">Active slider image with title</div>
  <svg class="abs slider-arrows" width="30" height="16" viewBox="0 0 30 16" aria-hidden="true">
    <path d="M8 2L2 8l6 6M22 2l6 6-6 6" fill="none" stroke="#fff" stroke-width="2" opacity="0.85"/>
  </svg>
</section>

<section class="abs slide-titles">
  <div class="band-a"><span>Slider title 1</span></div>
  <div class="band-b"><span>Slider title 2</span></div>
  <div class="band-a"><span>Slider title 3</span></div>
  <div class="band-b"><span>Slider title 4</span></div>
</section>

<div class="abs dropdown menu-main">
  <div>Menu item idle</div>
  <div class="sub">Menu item idle with subcategory</div>
  <div class="hover sub">Menu item hover</div>
  <div class="active">Menu item clicked</div>
</div>
<div class="abs dropdown menu-sub">
  <div>Menu item idle</div>
  <div>Menu item idle with category</div>
  <div>Menu item idle with category</div>
  <div>Menu item regular</div>
</div>

<aside class="abs categories">
  <h2>PRODUCT CATEGORIES</h2>
  <ul>
    <li>Product 1</li><li>Product 2</li><li>Product 3</li>
    <li>Product 4</li><li>Product 5</li><li>Product 6</li>
    <li>Product 7</li><li>Product 8</li><li>Product 9</li>
  </ul>
  <a class="abs more-link">more products</a>
</aside>

<div class="abs product" style="left:266px;top:457px"><div class="thumb"></div><div class="name">Item on sale 1</div><div class="price"><span class="old">$60</span>$30</div><div class="badge">-50%</div></div>
<div class="abs product" style="left:501px;top:457px"><div class="thumb"></div><div class="name">Item on sale 1</div><div class="price"><span class="old">$60</span>$30</div><div class="badge">-50%</div></div>
<div class="abs product" style="left:732px;top:457px"><div class="thumb"></div><div class="name">Item on sale 1</div><div class="price"><span class="old">$60</span>$30</div><div class="badge">-50%</div></div>

<div class="abs product" style="left:266px;top:518px"><div class="thumb"></div><div class="name">Item on sale 1</div><div class="price"><span class="old">$60</span>$30</div><div class="badge">-50%</div></div>
<div class="abs product" style="left:501px;top:518px"><div class="thumb"></div><div class="name">Item on sale 1</div><div class="price"><span class="old">$60</span>$30</div><div class="badge">-50%</div></div>
<div class="abs product" style="left:732px;top:518px"><div class="thumb"></div><div class="name">Item on sale 1</div><div class="price"><span class="old">$60</span>$30</div><div class="badge">-50%</div></div>

<div class="abs product" style="left:266px;top:581px"><div class="thumb"></div><div class="name">Item on sale 1</div><div class="price"><span class="old">$60</span>$30</div><div class="badge">-50%</div></div>
<div class="abs product" style="left:501px;top:581px"><div class="thumb"></div><div class="name">Item on sale 1</div><div class="price"><span class="old">$60</span>$30</div><div class="badge">-50%</div></div>
<div class="abs product" style="left:732px;top:581px"><div class="thumb"></div><div class="name">Item on sale 1</div><div class="price"><span class="old">$60</span>$30</div><div class="badge">-50%</div></div>

<div class="abs product bare" style="left:266px;top:643px"><div class="name">Item on sale 1</div><div class="badge">-50%</div></div>
<div class="abs product bare" style="left:501px;top:643px"><div class="name">Item on sale 1</div><div class="badge">-50%</div></div>
<div class="abs product bare" style="left:732px;top:643px"><div class="name">Item on sale 1</div><div class="badge">-50%</div></div>

<aside class="abs recent">
  <h3>RECENT PRODUCTS</h3>
  <div class="recent-item"><div class="sq"></div><div class="t">50% OFF on all products, act now!</div><div class="ago">12 minutes ago</div><div class="p">$60</div></div>
  <div class="recent-item gold"><div class="sq"></div><div class="t">50% OFF on all products!</div><div class="ago">12 minutes ago</div><div class="p">$60</div></div>
  <div class="recent-item"><div class="sq"></div><div class="t">50% OFF on all products!</div><div class="ago">12 minutes ago</div><div class="p">$60</div></div>
  <div class="recent-item"><div class="sq"></div><div class="t">50% OFF on all products!</div><div class="ago">12 minutes ago</div><div class="p">$60</div></div>
</aside>

<article class="abs article" style="left:279px">
  <div class="media" role="img" aria-label="Article photo of electronics"></div>
  <h4></h4>
  <p>Lorem Ipsum is simply dummy text of the printing and typesetting industry. Lorem Ipsum has been the industry's standard dummy text ever since the 1500s, when an unknown printer took a galley of type and scrambled it to make a type specimen book. It has survived not only five centuries, but also the leap into electronic typesetting.</p>
</article>
<article class="abs article" style="left:491px">
  <div class="media" role="img" aria-label="Article photo of electronics"></div>
  <h4 class="link">Title here</h4>
  <p>Lorem Ipsum is simply dummy text of the printing and typesetting industry. Lorem Ipsum has been the industry's standard dummy text ever since the 1500s, when an unknown printer took a galley of type and scrambled it to make a type specimen book. It has survived not only five centuries, but also the leap into electronic typesetting.</p>
</article>
<article class="abs article" style="left:704px">
  <div class="media" role="img" aria-label="Article photo of electronics"></div>
  <h4>Title here</h4>
  <p>Lorem Ipsum is simply dummy text of the printing and typesetting industry. Lorem Ipsum has been the industry's standard dummy text ever since the 1500s, when an unknown printer took a galley of type and scrambled it to make a type specimen book. It has survived not only five centuries, but also the leap into electronic typesetting.</p>
</article>

<footer>
  <div class="abs footer-links">Home<span>|</span>Product Directory<span>|</span>My Account<span>|</span>Easy Returns<span>|</span>Affiliate Program</div>
  <div class="abs copyright">Copyright © <u>Companyname</u>, 2005. All Rights Reserved</div>
  <div class="abs footer-rule"></div>
  <svg class="abs pay-badges" width="136" height="26" viewBox="0 0 136 26" aria-label="Accepted payment methods" role="img">
    <rect x="0.5" y="3.5" width="52" height="19" rx="2" fill="#f4f4f4" stroke="var(--badge-line)"/>
    <rect x="2.5" y="5.5" width="48" height="15" rx="1.5" fill="none" stroke="#c4c4c4"/>
    <rect x="56.5" y="6.5" width="24" height="16" rx="2" fill="#f4f4f4" stroke="var(--badge-line)"/>
    <rect x="84.5" y="5.5" width="24" height="17" rx="2" fill="#dedede" stroke="var(--badge-line)"/>
    <rect x="112.5" y="2.5" width="22" height="19" rx="2" fill="#e8e8e8" stroke="var(--badge-line)"/>
  </svg>
</footer>

</body>
</html>
```